Photography (and Videography) Flyer required

Am looking for an elegant and very professional looking flyer to promote Rowan Pell Photography which services for portrait, fashion, wedding and event photography - aswell as filmmaking, videography services for events such as weddings, conferences etc. The flyer is to be distributed in the New Year and as a promotional offer would like to have a tear off voucher included offering a 50% discount on all bookings. Would also like to include web address which is www.rowanpellphotography.example and email address which is enquiry@rowanpellphotography.example

(the website will be completed before the flyers are issued)

Target Market(s)

Young adults looking to get married soon and requiring professional photographer/videographer for wedding and related events Adult Males and Females in UK wanted personal fashion photographs of themselves in professional studio environment Parents of young children wanted professional portraits of their children Fashion designers, models, make up artisits looking for professional photographer/filmmaker

Industry/Entity Type

Fashion

Requirements
Must have
• Must be double sided A5 and include a tear off 50% off voucher. Include attractive looking people contained within
Nice to have
• Nice to have logo included
Should not have
• N/A

```html
<!DOCTYPE html>
<html lang="en">
<head>
<meta charset="utf-8">
<title>Rowan Pell Photography – A5 Flyer</title>
<link rel="stylesheet" href="https://fonts.googleapis.com/css2?family=Arimo:ital,wght@0,400;0,700;1,400&display=swap">
<style>
  :root {
    --plum: #5e0f5c;
    --plum-light: #7d2a7b;
    --plum-deep: #3f0a3e;
    --orchid: #b84fb5;
    --ink: #000000;
    --paper: #ffffff;
    --soft: #d9d9d9;
    --backdrop: #ebe7e1;
  }
  * { box-sizing: border-box; margin: 0; padding: 0; }
  html, body { width: 1200px; height: 900px; overflow: hidden; }
  body {
    background: var(--backdrop);
    font-family: "Arimo", Arial, sans-serif;
    color: var(--paper);
    position: relative;
  }
  .flyer {
    position: absolute;
    top: 40px;
    width: 570px;
    height: 820px;
    background: var(--ink);
    overflow: hidden;
    box-shadow: 0 4px 14px rgba(0,0,0,0.25);
  }
  .flyer--front { left: 15px; }
  .flyer--back { left: 615px; }

  .header {
    position: absolute; left: 0; top: 0; width: 100%; height: 160px;
    background: linear-gradient(180deg, var(--plum-light) 0%, var(--plum) 60%, var(--plum-deep) 100%);
  }
  .voucher-corner { position: absolute; top: 0; width: 160px; height: 160px; }
  .flyer--front .voucher-corner { right: 0; }
  .flyer--back .voucher-corner { left: 0; }
  .voucher-text {
    position: absolute; top: 34px; width: 130px; text-align: center; line-height: 1;
  }
  .flyer--front .voucher-text { right: -6px; transform: rotate(45deg); }
  .flyer--back .voucher-text { left: -6px; transform: rotate(-45deg); }
  .voucher-text .pct { font-weight: 700; font-size: 34px; display: block; }
  .voucher-text .word { font-size: 15px; display: block; margin-top: 2px; }
  .voucher-text .note { font-style: italic; font-size: 14px; display: block; }

  .brand {
    position: absolute; display: flex; align-items: center; gap: 12px;
    font-size: 28px; font-weight: 400; color: var(--paper);
  }
  .flyer--front .brand { left: 24px; top: 62px; }
  .flyer--back .brand { right: 22px; top: 92px; }
  .brand-dot { width: 14px; height: 14px; border-radius: 50%; background: var(--paper); flex: none; }

  .contact-row {
    position: absolute; left: 0; top: 172px; width: 100%;
    display: flex; justify-content: space-between; padding: 0 14px;
    font-size: 13px; color: var(--orchid);
  }

  .offer { position: absolute; left: 22px; top: 300px; }
  .offer-pct { font-size: 72px; font-weight: 700; letter-spacing: -1px; line-height: 1; }
  .offer-word { font-size: 24px; margin-left: 8px; }
  .offer-sub { font-size: 31px; font-style: italic; color: var(--orchid); line-height: 1.1; margin-top: 4px; }

  .service { position: absolute; left: 26px; }
  .service--photo { top: 450px; }
  .service--video { top: 630px; }
  .service-lead { font-size: 44px; font-weight: 700; line-height: 0.95; letter-spacing: -0.5px; }
  .service-name { font-size: 38px; font-weight: 400; line-height: 1; letter-spacing: -0.5px; }
  .service-list {
    font-size: 20px; color: var(--orchid); text-align: center;
    margin-top: 18px; line-height: 1.25; width: 310px;
  }

  .photo { position: absolute; }
  .photo--front {
    left: 335px; top: 290px; width: 235px; height: 530px;
    background: radial-gradient(ellipse at 50% 35%, #cfcfcf 0%, #8a8a8a 40%, #2a2a2a 75%, #000 100%);
  }
  .photo--back {
    left: 205px; top: 600px; width: 365px; height: 220px;
    background: radial-gradient(ellipse at 45% 55%, #8a3f8a 0%, #5a2a45 45%, #2a1410 80%, #120808 100%);
  }

  .about { position: absolute; left: 14px; top: 260px; width: 212px; }
  .rule { height: 3px; width: 130px; margin: 0 auto;
    background: linear-gradient(90deg, transparent, var(--orchid), transparent); }
  .about p { font-size: 15.5px; line-height: 1.28; text-align: justify; margin: 16px 0; }

  .details { position: absolute; left: 255px; top: 305px; }
  .detail { margin-bottom: 22px; }
  .detail dt { font-size: 17px; color: var(--orchid); margin-bottom: 4px; }
  .detail dd { font-size: 17px; }
</style>
</head>
<body>

<section class="flyer flyer--front">
  <header class="header">
    <div class="brand"><span class="brand-dot"></span>Rowan Pell Photography</div>
    <svg class="voucher-corner" viewBox="0 0 160 160" aria-hidden="true">
      <line x1="0" y1="0" x2="160" y2="160" stroke="#000" stroke-width="5" stroke-dasharray="12 8"/>
    </svg>
    <div class="voucher-text">
      <span class="pct">50%</span>
      <span class="word">DISCOUNT</span>
      <span class="note">on all bookings</span>
    </div>
  </header>

  <div class="contact-row">
    <span>07700 900 482</span>
    <span>www.rowanpellphotography.example</span>
    <span>enquiry@rowanpellphotography.example</span>
  </div>

  <div class="offer">
    <div><span class="offer-pct">50%</span><span class="offer-word">DISCOUNT</span></div>
    <div class="offer-sub">ON ALL BOOKINGS</div>
  </div>

  <div class="service service--photo">
    <div class="service-lead">PROMOTION</div>
    <div class="service-name">PHOTOGRAPHY</div>
    <div class="service-list">PORTRAIT, FASHION,<br>WEDDING, EVENT COVERAGE</div>
  </div>

  <div class="service service--video">
    <div class="service-lead">PROMOTION</div>
    <div class="service-name">VIDEOGRAPHY</div>
    <div class="service-list">FILM-MAKING, CONFERENCE,<br>WEDDING, EVENT COVERAGE</div>
  </div>

  <div class="photo photo--front" role="img" aria-label="Black and white studio portrait of a blonde woman in a trench coat, seated, hair blowing"></div>
</section>

<section class="flyer flyer--back">
  <header class="header">
    <svg class="voucher-corner" viewBox="0 0 160 160" aria-hidden="true">
      <line x1="160" y1="0" x2="0" y2="160" stroke="#000" stroke-width="5" stroke-dasharray="12 8"/>
    </svg>
    <div class="voucher-text">
      <span class="pct">50%</span>
      <span class="word">DISCOUNT</span>
      <span class="note">on all bookings</span>
    </div>
    <div class="brand"><span class="brand-dot"></span>Rowan Pell Photography</div>
  </header>

  <div class="about">
    <div class="rule"></div>
    <p>Portrait, Fashion and Wedding Photographer. Based in the Heart of the Midlands, with private studio located minutes from Birmingham City Centre. Specialising in creative, contemporary photographic and film production services throughout the UK</p>
    <p>The images captured are full of style, creativity and artistic flair giving you a spectacular collection of photographs, videos to remember your special occasions by.</p>
    <div class="rule"></div>
  </div>

  <dl class="details">
    <div class="detail"><dt>WEBSITE:</dt><dd>www.rowanpellphotography.example</dd></div>
    <div class="detail"><dt>EMAIL:</dt><dd>enquiry@rowanpellphotography.example</dd></div>
    <div class="detail"><dt>PHONE:</dt><dd>07700 900 482</dd></div>
  </dl>

  <div class="photo photo--back" role="img" aria-label="Colour portrait of a woman in a purple dress and sheer wrap, reclining on a brown leather sofa"></div>
</section>

</body>
</html>
```